Postcard Design

Domestic home cleaning business.......looking to call it " quiet lark nest" I would like to have a brivanto bottle as the main feature.....on the bottle the centre lable shoild read I'M YOUR ALL PURPOSE CLEANER above the lable should read DON'T LIFT A FINGER! Then opposite the bottle 5 bullet points House Keeping, Washing,Ironing bed changing, END OF TENANCY CLEANS, MOVING IN CLEANS spring cleans.

On the back of the card Iwould like to list the following: At the top of the card it should read
THE ALL PURPOSE PERSONALISED CLEANER AND WHAT YOU CAN EXPECT

Reliable
Police checked and referenced cleaners
SAME CLEANER EVERY WEEK ON THE SAME DAY AND TIME TO BE AGREED BY YOU
ONLY EVER USE CUSTOMERS OWN PRODUCTS
EACH CLEAN INSURED
GENERAL HOUSE CLEANING AS WELL AS IRONING IF REQUIRED (min 2hours per week)

Reason: I have a couple of hospital appointments to attend this week after s major operation, so I need more time to concentrate......sorry

```html
<!DOCTYPE html>
<html lang="en">
<head>
<meta charset="utf-8">
<title>Quiet Lark Nest 3 – Postcard</title>
<link rel="stylesheet" href="https://fonts.googleapis.com/css2?family=Kaushan+Script&family=Dancing+Script:wght@600&family=Open+Sans:wght@400;600;700&family=Architects+Daughter&family=Comfortaa:wght@400;700&family=Oswald:wght@500;600&display=swap">
<style>
  :root {
    --page: #ffffff;
    --sky-top: #1f3fb0;
    --sky-mid: #5f9fe0;
    --sky-light: #cfe6f7;
    --grass: #5f9b2a;
    --grass-dark: #3d7418;
    --lime: #d8f32a;
    --white: #ffffff;
    --note: #fbe98a;
    --note-edge: #f2d95a;
    --ink-blue: #1b48b8;
    --pin: #d8202a;
    --pin-shine: #ff8a8a;
    --bottle: #35b7c9;
    --bottle-deep: #1e8fa3;
    --glove: #e9ea1c;
    --teal: #2aa6c4;
    --teal-deep: #1689a8;
    --water: #b9e3f1;
    --water-deep: #7fc6de;
    --heading-blue: #1a2fc9;
    --list-navy: #13286e;
    --lettering-yellow: #e4f04a;
  }
  * { box-sizing: border-box; margin: 0; padding: 0; }
  html, body { width: 827px; height: 1200px; overflow: hidden; background: var(--page); }
  .canvas { position: relative; width: 827px; height: 1200px; }

  /* Front card */
  .card-front {
    position: absolute; left: 40px; top: 28px; width: 747px; height: 578px;
    overflow: hidden; box-shadow: 0 4px 14px rgba(0,0,0,.35);
  }
  .front-scene {
    position: absolute; inset: 0;
    background: linear-gradient(180deg, var(--sky-top) 0%, var(--sky-mid) 38%, var(--sky-light) 62%, var(--grass) 70%, var(--grass-dark) 100%);
  }
  .brand-name {
    position: absolute; left: 78px; top: 18px;
    font-family: "Kaushan Script", cursive; font-weight: 400; font-size: 46px; color: var(--lime);
  }
  .tagline {
    position: absolute; left: 26px; top: 96px;
    font-family: "Dancing Script", cursive; font-size: 22px; color: var(--white);
  }
  .intro {
    position: absolute; left: 26px; top: 130px; width: 465px;
    font-family: "Open Sans", sans-serif; font-variant: small-caps; font-size: 15.5px;
    line-height: 22.5px; color: var(--white); letter-spacing: .6px;
  }
  .service-note {
    position: absolute; left: 40px; top: 272px; width: 308px; height: 294px;
    background: var(--note); border-bottom: 3px solid var(--note-edge);
    transform: rotate(-2.5deg); box-shadow: 2px 4px 8px rgba(0,0,0,.3);
    padding: 24px 14px 0 16px;
  }
  .note-pin { position: absolute; left: 190px; top: 244px; width: 40px; height: 40px; }
  .service-list {
    list-style: none; font-family: "Architects Daughter", cursive;
    font-variant: small-caps; font-size: 21px; color: var(--ink-blue);
  }
  .service-list li { display: flex; gap: 12px; line-height: 25px; margin-bottom: 8px; }
  .service-list .tick { flex: none; width: 16px; height: 22px; }
  .product-visual {
    position: absolute; left: 528px; top: 16px; width: 210px; height: 372px;
    border-radius: 40px 40px 30px 30px;
    background: linear-gradient(160deg, var(--glove) 0%, var(--glove) 22%, var(--bottle) 40%, var(--bottle-deep) 100%);
  }
  .contact-list {
    position: absolute; left: 390px; top: 414px; list-style: none;
    font-family: "Open Sans", sans-serif; font-weight: 700; color: var(--white);
  }
  .contact-list li { display: flex; align-items: center; gap: 14px; height: 38px; }
  .contact-list svg { width: 22px; height: 22px; flex: none; }
  .contact-web, .contact-mail { font-size: 17px; }
  .contact-phone { font-size: 23px; }

  /* Back card */
  .card-back {
    position: absolute; left: 40px; top: 632px; width: 747px; height: 548px;
    overflow: hidden; box-shadow: 0 4px 14px rgba(0,0,0,.35);
  }
  .water-texture {
    position: absolute; inset: 0;
    background: radial-gradient(circle at 30% 70%, var(--water) 0%, var(--water-deep) 100%);
  }
  .hero-band {
    position: absolute; left: 20px; top: 18px; width: 707px; height: 282px;
    background: linear-gradient(180deg, var(--teal) 0%, var(--teal-deep) 100%);
  }
  .hero-question {
    position: absolute; left: 110px; top: 52px; font-family: "Comfortaa", sans-serif; color: var(--white);
  }
  .q-lead { display: block; font-size: 30px; }
  .q-mid { display: block; margin-left: 70px; font-size: 15px; color: var(--lettering-yellow); }
  .q-big { display: block; margin-left: 116px; margin-top: -6px; font-size: 34px; color: var(--lettering-yellow); }
  .q-tail { display: block; margin-left: 214px; margin-top: -4px; font-size: 15px; }
  .q-tail u { font-weight: 700; }
  .expect-panel {
    position: absolute; left: 20px; top: 300px; width: 707px; height: 228px;
    background: linear-gradient(180deg, rgba(255,255,255,.7), rgba(255,255,255,.35));
  }
  .expect-heading {
    position: absolute; left: 70px; top: 300px; transform: rotate(-3deg);
    font-family: "Oswald", sans-serif; font-weight: 600; font-size: 21px; color: var(--heading-blue);
  }
  .expect-list {
    position: absolute; left: 56px; top: 348px; list-style: none; transform: rotate(-3deg);
    font-family: "Oswald", sans-serif; font-weight: 500; font-size: 18px; line-height: 27px; color: var(--list-navy);
  }
  .expect-list li::before { content: "\25C6"; font-size: 12px; margin-right: 14px; vertical-align: 2px; }
  .expect-list .note-line { padding-left: 30px; font-size: 16px; }
  .expect-list .note-line::before { content: none; }
</style>
</head>
<body>
<main class="canvas">

  <section class="card-front">
    <div class="front-scene" role="img" aria-label="Blue sky with sunlight over a green grass field"></div>
    <h1 class="brand-name">Quiet Lark Nest 3</h1>
    <p class="tagline">High Quality Cleaning Service for your home.</p>
    <p class="intro">With more than 10 years experience we are a highly recommended and respected cleaning service, providing you with a cleaner who will understand and meet your needs. We will clean your home like it was our own – to perfection, and we guarantee you will be 100% satisfied.</p>

    <div class="service-note">
      <ul class="service-list">
        <li><svg class="tick" viewBox="0 0 16 22"><path d="M2 12 L6 19 L14 3" fill="none" stroke="var(--ink-blue)" stroke-width="2.6" stroke-linecap="round"/></svg>House Keeping</li>
        <li><svg class="tick" viewBox="0 0 16 22"><path d="M2 12 L6 19 L14 3" fill="none" stroke="var(--ink-blue)" stroke-width="2.6" stroke-linecap="round"/></svg>Washing, Ironing, Bed Changing</li>
        <li><svg class="tick" viewBox="0 0 16 22"><path d="M2 12 L6 19 L14 3" fill="none" stroke="var(--ink-blue)" stroke-width="2.6" stroke-linecap="round"/></svg>End of Tenancy Cleans</li>
        <li><svg class="tick" viewBox="0 0 16 22"><path d="M2 12 L6 19 L14 3" fill="none" stroke="var(--ink-blue)" stroke-width="2.6" stroke-linecap="round"/></svg>Move-in Cleans</li>
        <li><svg class="tick" viewBox="0 0 16 22"><path d="M2 12 L6 19 L14 3" fill="none" stroke="var(--ink-blue)" stroke-width="2.6" stroke-linecap="round"/></svg>Spring Cleans</li>
        <li><svg class="tick" viewBox="0 0 16 22"><path d="M2 12 L6 19 L14 3" fill="none" stroke="var(--ink-blue)" stroke-width="2.6" stroke-linecap="round"/></svg>New Development Cleans</li>
        <li><svg class="tick" viewBox="0 0 16 22"><path d="M2 12 L6 19 L14 3" fill="none" stroke="var(--ink-blue)" stroke-width="2.6" stroke-linecap="round"/></svg>Key-Holder Cleans</li>
      </ul>
    </div>
    <svg class="note-pin" viewBox="0 0 40 40"><circle cx="20" cy="18" r="13" fill="var(--pin)"/><circle cx="16" cy="14" r="4" fill="var(--pin-shine)"/></svg>

    <div class="product-visual" role="img" aria-label="Yellow-gloved hand holding a turquoise Brivanto spray bottle with a green front label"></div>

    <ul class="contact-list">
      <li class="contact-web"><svg viewBox="0 0 22 22"><circle cx="11" cy="11" r="9.5" fill="none" stroke="var(--lime)" stroke-width="2"/><rect x="10" y="9" width="2.4" height="7" fill="var(--lime)"/><circle cx="11.2" cy="6" r="1.4" fill="var(--lime)"/></svg>WWW.QUIETLARKNEST3.CO.UK</li>
      <li class="contact-phone"><svg viewBox="0 0 22 22"><path d="M2 8 Q11 1 20 8 L17 11 L14 8 L8 8 L5 11 Z" fill="var(--lime)"/><rect x="5" y="12" width="12" height="7" rx="2" fill="none" stroke="var(--lime)" stroke-width="2"/></svg>01632 960458</li>
      <li class="contact-phone"><svg viewBox="0 0 22 22"><rect x="6" y="1" width="10" height="20" rx="2" fill="none" stroke="var(--lime)" stroke-width="2"/><circle cx="11" cy="17" r="1.3" fill="var(--lime)"/></svg>07700 900440</li>
      <li class="contact-mail"><svg viewBox="0 0 22 22"><rect x="2" y="5" width="18" height="13" fill="none" stroke="var(--lime)" stroke-width="2"/><path d="M2 5 L11 12 L20 5" fill="none" stroke="var(--lime)" stroke-width="2"/></svg>QUIETLARKNEST3@LARKPOST.CO.UK</li>
    </ul>
  </section>

  <section class="card-back">
    <div class="water-texture" role="img" aria-label="Pale blue background covered in water droplets"></div>
    <div class="hero-band" role="img" aria-label="Illustration of uniformed cleaners dusting, mopping, washing windows, vacuuming and cleaning a bath, with a host gesturing"></div>
    <p class="hero-question">
      <span class="q-lead">what if...</span>
      <span class="q-mid">your house was</span>
      <span class="q-big">perfectly clean</span>
      <span class="q-tail">and <u>YOU</u> didn't lift a finger?</span>
    </p>
    <div class="expect-panel"></div>
    <h2 class="expect-heading">THE ALL PURPOSE PERSONALISED CLEANER and WHAT YOU CAN EXPECT</h2>
    <ul class="expect-list">
      <li>RELIABLE, POLICE CHECKED AND REFERENCED CLEANERS</li>
      <li>SAME CLEANER EVERY WEEK ON THE SAME DAY AND TIME AGREED to</li>
      <li>ONLY USE CUSTOMER'S OWN PRODUCTS</li>
      <li>EACH CLEAN INSURED</li>
      <li>GENERAL HOUSE CLEANING AS WELL AS IRONING IF REQUIRED</li>
      <li class="note-line">(min 2 hours per week)</li>
    </ul>
  </section>

</main>
</body>
</html>
```